Flyer-Design für KFZ Onlineshop
Zielgruppe
Wir sind ein reiner Onlineshop, der sich auf Teile für das optische Auftreten von Fahrzeugen spezialisiert hat. Unsere vier verschiedenen Kategorien sind:
Fahrwerkstechnik, Aerodynamik (Anbauteile), Reinigungs- und Pflegemittel und Sonstiges (3D Kennzeichen, Kennzeichenhalterungen, Radbefestigungen, Gutscheine,..).
Aufgabenstellung
Der Flyer sollte das Format 10,5 x 21 cm (DIN lang) haben.
Die Kategorien sollten auf dem Flyer stehen, zusätzlich unsere Anschrift und unser vorhandenes Logo.
Schriftart: Einige Texte bitte in den Schriftarten 'Formation Sans Regular' und 'BankGothic Lt BT'.
Farben: C=0, M=0, Y=0, K=80 (Grau), C=100, M=20, Y=0, K=0 (Blau)

```html
<!DOCTYPE html>
<html lang="de">
<head>
<meta charset="utf-8">
<title>Onlineshop Flyer</title>
<link rel="stylesheet" href="https://fonts.googleapis.com/css2?family=Michroma&family=Syncopate:wght@400&display=swap">
<style>
  :root {
    --brand-blue: #0094d8;
    --brand-grey: #58595b;
    --text-dark: #3d3d3f;
    --logo-grey: #4b4b4d;
    --pale-blue: #d8edf8;
    --paler-blue: #e8f5fc;
    --pale-grey: #ececec;
    --paler-grey: #f3f3f3;
    --white: #ffffff;
  }
  * { margin: 0; padding: 0; box-sizing: border-box; }
  html, body { width: 1200px; height: 2400px; overflow: hidden; background: var(--white); }
  .flyer { position: relative; width: 1200px; height: 2400px; overflow: hidden; background: var(--white); }
  .backdrop { position: absolute; inset: 0; width: 1200px; height: 2400px; }
  .logo-text {
    position: absolute; left: 108px; top: 402px;
    font-family: "Michroma", sans-serif; font-size: 88px; letter-spacing: 10px;
    color: var(--logo-grey); line-height: 1; white-space: nowrap;
  }
  .headline {
    position: absolute; left: 128px; top: 670px;
    font-family: "Michroma", sans-serif; font-size: 86px; letter-spacing: 9px;
    color: var(--brand-blue); line-height: 1; white-space: nowrap;
  }
  .tagline {
    position: absolute; left: 250px; top: 790px; width: 900px;
    font-family: "Syncopate", sans-serif; font-size: 40px; letter-spacing: 4px;
    color: var(--text-dark); line-height: 81px;
  }
  .tagline { left: 250px; }
  .divider {
    position: absolute; left: 242px; top: 1050px; width: 916px; height: 2px;
    background: var(--brand-grey);
  }
  .categories { position: absolute; left: 0; top: 1168px; list-style: none; }
  .category {
    position: relative; padding-left: 321px; height: 64px;
    font-family: "Syncopate", sans-serif; font-size: 34px; letter-spacing: 3px;
    color: var(--text-dark); line-height: 44px; white-space: nowrap;
  }
  .category-marker {
    position: absolute; left: 246px; top: 6px; width: 34px; height: 30px;
  }
  .subcategories { position: absolute; left: 503px; top: 1430px; list-style: none; }
  .subcategory {
    height: 54.5px;
    font-family: "Syncopate", sans-serif; font-size: 27px; letter-spacing: 3px;
    color: var(--text-dark); line-height: 36px; white-space: nowrap;
  }
  .subcategory:nth-child(n+2) { padding-left: 6px; }
  .address {
    position: absolute; left: 0; top: 2200px; width: 1200px; text-align: center;
    font-family: "Syncopate", sans-serif; font-size: 32px; letter-spacing: 4px;
    color: var(--white); line-height: 87px;
  }
</style>
</head>
<body>
<main class="flyer">
  <svg class="backdrop" viewBox="0 0 508 1016" preserveAspectRatio="none" aria-hidden="true">
    <polygon points="0,54 508,54 508,181 0,100" fill="var(--paler-blue)"/>
    <polygon points="0,54 508,54 508,100 0,244" fill="var(--pale-blue)" opacity="0.7"/>
    <rect x="0" y="0" width="508" height="54" fill="var(--brand-blue)"/>
    <polygon points="208,54 305,54 256,109" fill="var(--brand-blue)"/>
    <polygon points="0,772 508,664 508,850 0,850" fill="var(--paler-grey)"/>
    <polygon points="0,790 260,850 0,850" fill="var(--pale-grey)"/>
    <polygon points="150,820 508,790 508,850 60,850" fill="var(--pale-grey)" opacity="0.6"/>
    <rect x="0" y="850" width="508" height="166" fill="var(--brand-grey)"/>
    <polygon points="208,850 305,850 256,904" fill="var(--pale-grey)"/>
    <path class="pin-icon" d="M256,856 a6,6 0 0 1 6,6 c0,4.5 -6,11 -6,11 c0,0 -6,-6.5 -6,-11 a6,6 0 0 1 6,-6 z M256,859.5 a2.4,2.4 0 1 0 0.01,0 z" fill="var(--brand-grey)" fill-rule="evenodd"/>
  </svg>

  <div class="logo-text">YOUR LOGO</div>
  <h1 class="headline">ONLINESHOP</h1>
  <p class="tagline" style="left:250px">sich auf Teile für das<br>optische</p>
  <div class="divider"></div>

  <ul class="categories">
    <li class="category"><svg class="category-marker" viewBox="0 0 34 30"><path d="M2,3 L12,15 L2,27 M16,3 L26,15 L16,27" fill="none" stroke="var(--brand-blue)" stroke-width="4"/></svg>Fahrwerkstechnik</li>
    <li class="category"><svg class="category-marker" viewBox="0 0 34 30"><path d="M2,3 L12,15 L2,27 M16,3 L26,15 L16,27" fill="none" stroke="var(--brand-blue)" stroke-width="4"/></svg>Aerodynamik (Anbauteile)</li>
    <li class="category"><svg class="category-marker" viewBox="0 0 34 30"><path d="M2,3 L12,15 L2,27 M16,3 L26,15 L16,27" fill="none" stroke="var(--brand-blue)" stroke-width="4"/></svg>Reinigungs- und Pflegemittel</li>
    <li class="category"><svg class="category-marker" viewBox="0 0 34 30"><path d="M2,3 L12,15 L2,27 M16,3 L26,15 L16,27" fill="none" stroke="var(--brand-blue)" stroke-width="4"/></svg>Sonstiges</li>
  </ul>

  <ul class="subcategories">
    <li class="subcategory">- 3D Kennzeichen</li>
    <li class="subcategory">- Kennzeichenhalterungen</li>
    <li class="subcategory">- Radbefestigungen</li>
    <li class="subcategory">- Gutscheine</li>
    <li class="subcategory">- ..............</li>
  </ul>

  <address class="address" style="font-style:normal">Lindenweg 27,<br>80331 München</address>
</main>
</body>
</html>
```